Lead Sales Portal Needs to Generate B2B Signup's

We are looking for banner ad designs to drive new business (B2B) traffic to our insurance and mortgage industry self serve lead sites. The sites are HomeLoanProspectHub.com and PolicyBuyerHub.com, and we service over 45,000 insurance agents and mortgage lenders in a self serve lead portal model. We want our banners to generate more of these clients.

Our clients come to our sites, browse our database and then pick out and purchase the consumer leads that they need to generate new business.

We advertise extensively on Zyntrix and on other PPC platforms, and our existing banners are looking really tired.

Some of the ad copy that works well for us is:

Cherry Pick Your Life Leads - Why Pay More Than $3.50 For Life Insurance Leads?
Sign up today and we'll match up to $250

Agents - Here's $250 For New Clients. Cherry Pick Your Life Insurance Leads & Save! Sign up today and we'll match up to $250

One of our Landing Pages that performs well is here:
http://www.policybuyerhub.com/lp/008/

One of our competitors ad's are here:

http://www.brellow.com/search/results?q=QuoteMarten&ad=427360

We're looking for a design that is eye catching, uses our "Deeply Discounted Leads" and our "$250 match bonus"

This is the second contest that we have for the same sites. The previous designs were great and really performed well, so we are looking for new designs now that 6 months have passed. I have uploaded some winning banners from the last group for your information.

Reason: I've been asked by some of the designers to delay a day to get their designs in. I'm happy to do it!

Target Market(s)

These are insurance agents and mortgage lenders. All of our clients are business' or individuals within the business. This is a B2B campaign, so we need something that is professional and upscale. These are NOT consumer facing ad's!

Industry/Entity Type

Insurance

Font styles to use
Sans Serif

Requirements
Must have
• We must have the logos for the sites in the banners. Also, we must have a call to action arrow and "Go" button. Some animation is necessary, (especially around the arrow and the GO button).

One or two designs.

File type

.JPEG
.JPG
.PNG
.GIF

File size

150 KB or smaller

Image sizes

Vertical rectangle: 240 x 400
Mobile leaderboard: 320 x 50
Banner: 468 x 60
Leaderboard: 728 x 90
Square: 250 x 250
Small square: 200 x 200
Large rectangle: 336 x 280
Inline rectangle: 300 x 250
Skyscraper: 120 x 600
Wide skyscraper: 160 x 600
Half-page: 300 x 600
Large leaderboard: 970 x 90

```html
<!DOCTYPE html>
<html lang="en">
<head>
<meta charset="utf-8">
<title>Policy Buyer Hub – Banner Set</title>
<link rel="stylesheet" href="https://fonts.googleapis.com/css2?family=Arimo:wght@400;700&display=swap">
<style>
  :root {
    --page-bg: #ffffff;
    --green-light: #a6d13a;
    --green-dark: #5c9a12;
    --title-green: #4f850c;
    --title-halo: #d9efa6;
    --orange-light: #ffb534;
    --orange-dark: #f07a06;
    --dark-top: #3a3a3a;
    --dark-bottom: #141414;
    --panel-white: #ffffff;
    --panel-grey: #dcdcdc;
    --ink: #333333;
    --button-ink: #3b2208;
    --accent-red: #e8262b;
    --label-ink: #333333;
    --label-size: #f05a28;
    --photo-a: #c9d3dc;
    --photo-b: #5d6b7a;
  }
  * { margin: 0; padding: 0; box-sizing: border-box; }
  html, body { width: 1200px; height: 1200px; overflow: hidden; background: var(--page-bg); }
  body { font-family: "Arimo", Arial, sans-serif; position: relative; }

  .ad { position: absolute; display: block; font-family: "Arimo", Arial, sans-serif; font-weight: 700; }
  .ad--leaderboard { left: 78px; top: 47px; width: 1027px; height: 127px; }
  .ad--rectangle { left: 75px; top: 309px; width: 423px; height: 353px; }
  .ad--skyscraper { left: 876px; top: 236px; width: 226px; height: 846px; }

  .size-label { position: absolute; font-size: 23px; color: var(--label-ink); white-space: nowrap; }
  .size-label .file-size { color: var(--label-size); margin-left: 8px; }
  .size-label--leaderboard { left: 76px; top: 184px; }
  .size-label--rectangle { left: 74px; top: 671px; }
  .size-label--skyscraper { left: 885px; top: 1094px; }

  .title-text { fill: var(--title-green); stroke: var(--title-halo); stroke-width: 0.5; paint-order: stroke; text-anchor: middle; }
  .lead-text { fill: #ffffff; text-anchor: middle; }
  .panel-text { fill: var(--ink); text-anchor: middle; }
  .price { fill: var(--accent-red); }
  .button-label { fill: var(--button-ink); }
  .button-disc { fill: var(--button-ink); }
  .button-arrow { fill: none; stroke: #ffffff; stroke-width: 3.5; stroke-linecap: round; stroke-linejoin: round; }
  .logo-mark { fill: #1e1e1e; }
  .logo-name { fill: #1e1e1e; font-weight: 400; }
  .stop-green-light { stop-color: var(--green-light); }
  .stop-green-dark { stop-color: var(--green-dark); }
  .stop-orange-light { stop-color: var(--orange-light); }
  .stop-orange-dark { stop-color: var(--orange-dark); }
  .stop-dark-top { stop-color: var(--dark-top); }
  .stop-dark-bottom { stop-color: var(--dark-bottom); }
  .stop-panel-white { stop-color: var(--panel-white); }
  .stop-panel-grey { stop-color: var(--panel-grey); }
  .stop-photo-a { stop-color: var(--photo-a); }
  .stop-photo-b { stop-color: var(--photo-b); }
</style>
</head>
<body>

<svg width="0" height="0" style="position:absolute" aria-hidden="true">
  <defs>
    <linearGradient id="green-fill" x1="0" y1="0" x2="0" y2="1"><stop offset="0" class="stop-green-light"/><stop offset="1" class="stop-green-dark"/></linearGradient>
    <linearGradient id="orange-fill" x1="0" y1="0" x2="0" y2="1"><stop offset="0" class="stop-orange-light"/><stop offset="1" class="stop-orange-dark"/></linearGradient>
    <linearGradient id="dark-fill" x1="0" y1="0" x2="0" y2="1"><stop offset="0" class="stop-dark-top"/><stop offset="1" class="stop-dark-bottom"/></linearGradient>
    <linearGradient id="panel-fill" x1="0" y1="0" x2="0" y2="1"><stop offset="0" class="stop-panel-white"/><stop offset="1" class="stop-panel-grey"/></linearGradient>
    <linearGradient id="photo-fill" x1="0" y1="0" x2="1" y2="1"><stop offset="0" class="stop-photo-a"/><stop offset="1" class="stop-photo-b"/></linearGradient>
  </defs>
</svg>

<!-- Leaderboard 728 x 90 -->
<svg class="ad ad--leaderboard" viewBox="0 0 728 90" role="group" aria-label="Leaderboard banner">
  <rect class="ad-background" width="728" height="90" fill="url(#dark-fill)"/>
  <path class="chevron-edge" d="M148 0 H164 L184 45 L164 90 H148 L168 45 Z" fill="url(#orange-fill)"/>
  <path class="headline-panel" d="M0 0 H148 L168 45 L148 90 H0 Z" fill="url(#green-fill)"/>
  <g class="title-text" font-size="23">
    <text x="70" y="29">Cherry Pick</text>
    <text x="70" y="53">Your Life</text>
    <text x="70" y="77">Leads</text>
  </g>
  <g class="lead-text" font-size="13">
    <text x="215" y="25">Sign Up Today</text>
    <text x="215" y="42">and We’ll</text>
    <text x="215" y="59">Make up</text>
    <text x="215" y="76">To $250</text>
  </g>
  <rect class="brand-card" x="268" y="10" width="210" height="70" fill="#ffffff"/>
  <circle class="logo-mark" cx="280" cy="45" r="6"/>
  <text class="logo-name" x="289" y="48" font-size="8.5">Policy Buyer Hub</text>
  <rect class="team-photo" x="362" y="10" width="116" height="70" fill="url(#photo-fill)" role="img" aria-label="Photo of two smiling business people giving a thumbs up"/>
  <path class="offer-edge" d="M478 0 H574 Q602 45 574 90 H478 Z" fill="url(#orange-fill)"/>
  <path class="offer-panel" d="M478 0 H566 Q593 45 566 90 H478 Z" fill="url(#panel-fill)"/>
  <g class="panel-text" font-size="14">
    <text x="524" y="19">Sign Up</text>
    <text x="524" y="33">Today</text>
    <text x="524" y="49">and We’ll</text>
    <text x="524" y="63">Make up</text>
    <text x="524" y="78">To <tspan class="price">$250</tspan></text>
  </g>
  <path class="action-panel" d="M574 0 H728 V90 H574 Q602 45 574 0 Z" fill="url(#green-fill)"/>
  <g class="cta-button" transform="translate(583 28)">
    <rect width="135" height="42" rx="4" fill="url(#orange-fill)"/>
    <text class="button-label" x="10" y="26" font-size="14">Sign Up Now</text>
    <circle class="button-disc" cx="117" cy="21" r="15"/>
    <polyline class="button-arrow" points="113,13 121,21 113,29"/>
  </g>
</svg>
<div class="size-label size-label--leaderboard">728X90<span class="file-size">23.6 KB</span></div>

<!-- Inline rectangle 300 x 250 -->
<svg class="ad ad--rectangle" viewBox="0 0 300 250" role="group" aria-label="Rectangle banner">
  <rect class="ad-background" width="300" height="250" fill="url(#dark-fill)"/>
  <path class="chevron-edge" d="M0 24 L150 38 L300 24 V32 L150 47 L0 32 Z" fill="url(#orange-fill)"/>
  <path class="headline-panel" d="M0 0 H300 V24 L150 38 L0 24 Z" fill="url(#green-fill)"/>
  <text class="title-text" x="150" y="20" font-size="19">Cherry Pick Your Life Leads</text>
  <g class="lead-text" font-size="15">
    <text x="150" y="63">Receive $250 Worth Of Leads Today</text>
    <text x="150" y="80">by Just Sign Up</text>
  </g>
  <rect class="brand-card" x="25" y="88" width="252" height="78" rx="3" fill="#ffffff"/>
  <circle class="logo-mark" cx="41" cy="129" r="10"/>
  <text class="logo-name" x="55" y="133" font-size="12">Policy Buyer Hub</text>
  <rect class="team-photo" x="152" y="88" width="125" height="78" fill="url(#photo-fill)" role="img" aria-label="Photo of two smiling business people giving a thumbs up"/>
  <path class="offer-edge" d="M0 168 Q150 152 300 168 V200 H0 Z" fill="url(#orange-fill)"/>
  <path class="offer-panel" d="M0 176 Q150 162 300 176 V206 Q150 226 0 206 Z" fill="url(#panel-fill)"/>
  <path class="action-panel" d="M0 214 Q150 234 300 214 V250 H0 Z" fill="url(#green-fill)"/>
  <text class="panel-text" x="150" y="194" font-size="12">Sign Up Today and We’ll Make up To <tspan class="price">$250</tspan></text>
  <g class="cta-button" transform="translate(82 203)">
    <rect width="133" height="40" rx="4" fill="url(#orange-fill)"/>
    <text class="button-label" x="9" y="25" font-size="14">Sign Up Now</text>
    <circle class="button-disc" cx="115" cy="20" r="15"/>
    <polyline class="button-arrow" points="111,12 119,20 111,28"/>
  </g>
</svg>
<div class="size-label size-label--rectangle">300X250<span class="file-size">27.6 KB</span></div>

<!-- Wide skyscraper 160 x 600 -->
<svg class="ad ad--skyscraper" viewBox="0 0 160 600" role="group" aria-label="Skyscraper banner">
  <rect class="ad-background" width="160" height="600" fill="url(#dark-fill)"/>
  <path class="chevron-edge" d="M0 80 L80 118 L160 80 V93 L80 131 L0 93 Z" fill="url(#orange-fill)"/>
  <path class="headline-panel" d="M0 0 H160 V80 L80 118 L0 80 Z" fill="url(#green-fill)"/>
  <g class="title-text" font-size="25">
    <text x="80" y="30">Cherry Pick</text>
    <text x="80" y="56">Your Life</text>
    <text x="80" y="82">Leads</text>
  </g>
  <g class="lead-text" font-size="18">
    <text x="80" y="148">Receive $250</text>
    <text x="80" y="167">Worth Of</text>
    <text x="80" y="186">Leads Today</text>
    <text x="80" y="205">by Just</text>
    <text x="80" y="224">Sign Up</text>
  </g>
  <rect class="brand-card" x="12" y="238" width="136" height="200" rx="2" fill="#ffffff"/>
  <circle class="logo-mark" cx="27" cy="260" r="10"/>
  <text class="logo-name" x="41" y="264" font-size="11.5">Policy Buyer Hub</text>
  <rect class="team-photo" x="12" y="280" width="136" height="158" fill="url(#photo-fill)" role="img" aria-label="Photo of two smiling business people giving a thumbs up"/>
  <path class="offer-edge" d="M0 445 Q80 428 160 445 V480 H0 Z" fill="url(#orange-fill)"/>
  <path class="offer-panel" d="M0 452 Q80 437 160 452 V526 Q80 552 0 526 Z" fill="url(#panel-fill)"/>
  <path class="action-panel" d="M0 536 Q80 560 160 536 V600 H0 Z" fill="url(#green-fill)"/>
  <g class="panel-text" font-size="17">
    <text x="80" y="475">Sign Up Today</text>
    <text x="80" y="492">and We’ll</text>
    <text x="80" y="509">Make up</text>
    <text x="80" y="526">To <tspan class="price">$250</tspan></text>
  </g>
  <g class="cta-button" transform="translate(12 552)">
    <rect width="134" height="40" rx="4" fill="url(#orange-fill)"/>
    <text class="button-label" x="8" y="25" font-size="14">Sign Up Now</text>
    <circle class="button-disc" cx="116" cy="20" r="15"/>
    <polyline class="button-arrow" points="112,12 120,20 112,28"/>
  </g>
</svg>
<div class="size-label size-label--skyscraper">160X600<span class="file-size">37.0 KB</span></div>

</body>
</html>
```